Neukunden-Flyer für Yoga-&Massage
Zielgruppe
Yoga-Leherin, die Yoga nicht nur zur zeitweisen Entspannung vermittelt sondern als Ansatz dauerhafter Entschleunigung, Stressbewältigung und körperlicher Fitness. Thai Yoga Massage arbeitet nicht nur körperlich sondern auch energetisch auch auf der Herzebene.
Zielgruppe:
Jeder, der sich etwas Gutes tun will und seine Selbstheilungskräfte aktivieren und wieder mehr bei sich sein möchte.
Aufgabenstellung
Erstellung eines Flyers mit folgenden Eigenschaften:
• DIN A4 lang - Wickelfalz-Flyer 6-seitig
• Klare Formen und kräftige Farben
• Einprägsam
• Fließend
• CMYK - keine Sonderfarben
• Druckdatenvorlage (PSDs (außen/innen bzw. Druckdatenerstellung Fonts/Pfade
beachten)
Abgabe als offene Datei: PSD, AI bzw. als geschlossene Druckdatei X3 PDF.

```html
<!DOCTYPE html>
<html lang="de">
<head>
<meta charset="utf-8">
<title>ATEMRAUM – Flyer Innenseite</title>
<link href="https://fonts.googleapis.com/css2?family=Roboto:ital,wght@0,300;0,500;0,700;1,300&display=swap" rel="stylesheet">
<style>
  :root{
    --pink:#e2127a;
    --grey:#7b7b7b;
    --grey-dark:#6d6d6d;
    --lime:#ece98a;
    --paper:#ffffff;
    --stage:#e6e6e6;
    --mist:#eef3f6;
  }
  *{box-sizing:border-box;margin:0;padding:0}
  html,body{width:1200px;height:675px;overflow:hidden;background:var(--stage)}
  body{font-family:"Roboto",Arial,sans-serif;color:var(--grey)}
  .flyer{position:absolute;left:140px;top:10px;width:920px;height:654px;background:var(--paper);overflow:hidden}
  .inner-spread{position:absolute;left:0;top:0;width:611px;height:654px;
    background:linear-gradient(to bottom,var(--paper) 0,var(--paper) 250px,var(--mist) 262px,var(--paper) 560px)}
  .top-wave{position:absolute;left:0;top:0}
  .lotus-area{position:absolute;left:0;top:520px;width:370px;height:134px;
    background:radial-gradient(ellipse at 45% 60%,#dfe6ee 0,#eef2f6 45%,rgba(255,255,255,0) 75%)}
  .abs{position:absolute}
  .center{text-align:center}
  .panel-title{font-weight:300;font-size:33px;line-height:1;letter-spacing:.3px}
  .panel-title.pink{color:var(--pink)}
  .rule{position:absolute;height:1.5px}
  .rule.pink{background:var(--pink)}
  .rule.grey{background:var(--grey)}
  .bar{position:absolute;height:6px}
  .body-text{font-weight:500;font-size:13.5px;line-height:16px;color:var(--grey)}
  .lead{font-weight:700;font-size:17px;line-height:20px;color:var(--grey)}
  .subhead{font-weight:700;font-size:17px;line-height:19px;color:var(--grey)}
  .portrait{position:absolute;left:84px;top:219px;width:132px;height:132px;border-radius:50%;
    border:5px solid var(--pink);background:radial-gradient(circle at 55% 45%,#d9d9d9 0,#8e8e8e 55%,#3a3a3a 100%);
    box-shadow:0 3px 5px rgba(0,0,0,.35)}
  .signature{font-style:italic;font-weight:300;color:var(--pink)}
  .cover-photo{position:absolute;left:611px;top:295px;width:309px;height:359px;
    background:linear-gradient(to bottom,rgba(255,255,255,1) 0,rgba(240,220,222,.9) 22%,#e3b3b6 45%,#c98a95 65%,#a45a67 85%,#8c4552 100%)}
  .cover-photo::after{content:"";position:absolute;inset:0;
    background:linear-gradient(to right,rgba(120,140,190,.35) 0,rgba(255,255,255,0) 45%)}
  .brand-name{position:absolute;left:611px;top:172px;width:309px;text-align:center;
    font-weight:300;font-size:28px;letter-spacing:7px;color:var(--grey-dark)}
</style>
</head>
<body>
<main class="flyer">
  <section class="inner-spread">
    <svg class="top-wave" width="611" height="160" viewBox="0 0 611 160" aria-hidden="true">
      <path d="M0,0 H611 V103 C520,58 340,12 0,29 Z" fill="var(--lime)"/>
    </svg>
    <div class="lotus-area" role="img" aria-label="Weiße Lotusblüte auf ruhigem Wasser"></div>

    <!-- Panel: Über mich -->
    <h1 class="abs center panel-title pink" style="left:17px;top:76px;width:265px">ATEMRAUM</h1>
    <div class="rule pink" style="left:17px;top:110px;width:265px"></div>
    <p class="abs center body-text" style="left:5px;top:115px;width:290px">versteht sich als Kraftquelle<br>für körperliche Fitness, mentale Ruhe und<br>seelisches Gleichgewicht.</p>
    <div class="bar" style="left:113px;top:179px;width:73px;background:var(--pink)"></div>

    <svg class="abs" style="left:70px;top:205px" width="160" height="160" viewBox="0 0 160 160" aria-hidden="true">
      <circle cx="80" cy="80" r="78" fill="none" stroke="var(--pink)" stroke-width="2" stroke-dasharray="0.1 5" stroke-linecap="round"/>
    </svg>
    <div class="portrait" role="img" aria-label="Schwarzweiß-Porträt der Yogalehrerin"></div>

    <h2 class="abs center panel-title" style="left:17px;top:379px;width:265px;font-size:30px">Vita</h2>
    <div class="rule pink" style="left:17px;top:412px;width:265px"></div>
    <p class="abs body-text" style="left:15px;top:416px;width:275px">800 Stunden zertifizierte Sarvanam Lehrerin. Ausbildung bei Jonas Weidlich und Greta Holm. Laufende Assistenz bei Tobias Rainer (Ashtanga Loft).</p>
    <p class="abs body-text" style="left:15px;top:495px;width:280px">Ich unterrichte in Lindental Gruppen- &amp; Einzelkurse – unter anderem in den Yoga-Studios von Jonas Weidlich, Yoga-Lehrer der Fußball-Nationalmannschaft.</p>

    <!-- Panel: Termin & Kontakt -->
    <h2 class="abs center panel-title" style="left:318px;top:76px;width:275px">Termin &amp; Kontakt</h2>
    <div class="rule grey" style="left:323px;top:110px;width:265px"></div>
    <p class="abs center lead" style="left:310px;top:115px;width:290px">Vereinbaren Sie noch heute<br>einen Termin</p>
    <p class="abs body-text" style="left:321px;top:175px;width:290px">und erleben Sie, wie Sie durch individuelle Körperarbeit mehr zu sich selbst finden.</p>
    <div class="bar" style="left:416px;top:214px;width:73px;background:var(--grey)"></div>

    <div class="abs" style="left:318px;top:230px;width:290px">
      <h3 class="subhead">ATEMRAUM</h3>
      <p class="body-text">Lena Falkner<br>Birkenhofweg 14<br>12345 Lindental<br>E-Mail: hallo@atemraum-yoga.de<br>Mobil: 0151 - 20418836</p>
    </div>
    <div class="abs" style="left:318px;top:345px;width:290px">
      <h3 class="subhead">Anreise mit Auto:</h3>
      <p class="body-text">KASTANIENHOF - zentral in Lindental<br>Altstadt-Süd ggf. Rückseite finden sich fast immer Parkgelegenheiten</p>
    </div>
    <div class="abs" style="left:318px;top:428px;width:290px">
      <h3 class="subhead">Anreise mit Bus &amp; Bahn:</h3>
      <p class="body-text">Die Buslinien 132, N40, N41<br>(Haltestelle Lindenplatz)<br>sowie 53 (Haltestelle Marktkirche)<br>halten direkt vor der Tür.</p>
    </div>
    <p class="abs body-text" style="left:318px;top:526px;width:290px">Nur 5 Minuten zu Fuß sind U3, S7 und S27 (Haltestelle Südbahnhof) entfernt</p>

    <div class="abs center signature" style="left:367px;top:578px;width:220px">
      <p style="font-size:17px;line-height:20px">Ich freue mich auf Sie</p>
      <p style="font-size:12.5px;line-height:15px">Ihre</p>
      <p style="font-size:17px;line-height:22px">Lena Falkner</p>
    </div>
  </section>

  <!-- Titelseite -->
  <section aria-label="Titelseite">
    <div class="brand-name">ATEMRAUM</div>
    <div class="cover-photo" role="img" aria-label="Frau in Meditationshaltung am Kieselstrand im Abendlicht"></div>
  </section>
</main>
</body>
</html>
```